Tender Scout Letterhead Design Project

We need a letterhead design for a consultancy business based in Australia.

Tender Scout is a unique business designed to assist with the complex and time consuming nature of selecting contractors, showing them what to do and reviewing quotes when it comes to body corporate and strata maintenance items such as painting, waterproofing, plumbing and electrical.

Target Market(s)

apartment managers

Industry/Entity Type

Business

Requirements
Must have
• must have logo and contact details

Tender Scout
82 Wallaroo Creek Road
Yandara, QLD 4571
Ph 07 5391 2846
Fax 07 5327 6018
Mobile 0438 917304

```html
<!DOCTYPE html>
<html lang="en">
<head>
<meta charset="utf-8">
<title>Tender Scout Letterhead</title>
<link rel="stylesheet" href="https://fonts.googleapis.com/css2?family=Nunito+Sans:wght@400;700;800&display=swap">
<style>
  :root {
    --frame-green: #a6ce39;
    --paper: #ffffff;
    --ink: #231f20;
    --name-grey: #a7a9ac;
  }
  * { margin: 0; padding: 0; box-sizing: border-box; }
  html, body { width: 848px; height: 1200px; overflow: hidden; }
  body {
    background: var(--frame-green);
    font-family: "Nunito Sans", Arial, sans-serif;
    color: var(--ink);
  }
  .letterhead {
    position: absolute;
    left: 22px; top: 22px;
    width: 806px; height: 1156px;
    background: var(--paper);
    border-radius: 30px;
    overflow: hidden;
  }
  .brand {
    position: absolute;
    left: 60px; top: 44px;
    font-size: 54px;
    font-weight: 800;
    line-height: 1;
    color: var(--name-grey);
    letter-spacing: -0.5px;
    white-space: nowrap;
  }
  .contact {
    position: absolute;
    top: 14px;
    font-size: 14.5px;
    line-height: 20px;
    font-style: normal;
  }
  .contact-address { left: 435px; }
  .contact-name { font-weight: 800; }
  .contact-numbers { left: 671px; }
  .contact-numbers li {
    list-style: none;
    display: flex;
    align-items: center;
    gap: 6px;
  }
  .contact-numbers svg { width: 14px; height: 14px; fill: var(--ink); }
  .body-copy {
    position: absolute;
    left: 140px; top: 386px;
    width: 578px;
    font-size: 15px;
    line-height: 18.8px;
  }
  .body-copy p + p { margin-top: 18.8px; }
</style>
</head>
<body>
  <main class="letterhead">
    <header>
      <div class="brand">Tender Scout</div>

      <address class="contact contact-address">
        <div class="contact-name">Tender Scout</div>
        <div>82 Wallaroo Creek Road</div>
        <div>Yandara, QLD 4571</div>
      </address>

      <ul class="contact contact-numbers">
        <li>
          <svg viewBox="0 0 16 16" aria-label="Phone"><path d="M1 5c0-2 3-3 7-3s7 1 7 3v1h-4V4.5H5V6H1zM3 7h10l2 7H1z"/></svg>
          <span>07 5391 2846</span>
        </li>
        <li>
          <svg viewBox="0 0 16 16" aria-label="Fax"><path d="M4 1h8v4H4zM1 6h14v7h-3v2H4v-2H1zM5 10v4h6v-4z"/></svg>
          <span>07 5327 6018</span>
        </li>
        <li>
          <svg viewBox="0 0 16 16" aria-label="Mobile"><path d="M5 1h6a1 1 0 0 1 1 1v12a1 1 0 0 1-1 1H5a1 1 0 0 1-1-1V2a1 1 0 0 1 1-1zm.5 2v7h5V3z"/></svg>
          <span>0438 917304</span>
        </li>
      </ul>
    </header>

    <section class="body-copy">
      <p>When it comes to stormwater systems, the rule is “an ounce of prevention is worth a pound of cure.”&nbsp; It is much easier to pay for maintenance and proactive repairs of small issues before they develop into costly major repairs, or worse, violations.&nbsp;&nbsp; Your stormwater system has been designed to convey and filter the contaminants in your property's runoff.&nbsp;&nbsp; However, a malfunctioning stormwater system either floods, or simply dumps your property's contaminants into surface waters such as rivers or streams. To minimize this liability, you need a company with the skills, training, and experience to protect you from noncompliance.</p>
      <p>As state and federal agencies continue their crackdown on stormwater violations, companies of every size are turning to Clearflow Drainage Care to keep their stormwater program on track.&nbsp;&nbsp; They've seen they need more than the simple “mow, blow, and go” of the average landscaper.&nbsp; Without the certification and training t<br>to deal with BMPs, a landscaper may “scalp” the grass causing erosion that can lead to expensive washout repairs.&nbsp; Improperly controlled invasive plants can overrun a basin, leading to backups and flooding.&nbsp;&nbsp; And a mismanaged BMP can become a breeding ground for potentially disease carrying mosquitoes.&nbsp;&nbsp; With our help, this won't happen.</p>
      <p>Clearflow Drainage Care (C.D.C.) has the training, the experience, and the equipment to handle all phases of BMP maintenance and repair.&nbsp; We have the resources of a large company with the attention to detail of a small one, and this helps us maintain our commitment to unrivalled customer service.</p>
    </section>
  </main>
</body>
</html>
```